Sports Nutrition PRE-WORKOUT Product Label

We are Brandvik Laboratories, a new sports nutrition supplement company. Like most supplement jar/bottle designs, we need a standard label design for one product that can be later modified to be used for the other products. We'd like to develop a relationship with the winner so we can hire them for our future products as well, which will likely consist of modifying the same theme.
Our first product is a pre-workout called "IRON SURGE".
Our competitors include companies like Vantrexa, QPL and PowerGlynt. You can see there designs through google or sites like liftgrove.com.
Title text should be large and communicate STRENGTH and POWER.
Company logo variations are attached.
Label size: 11.125"W x 4.25"H
Bottle/LId color: Black
Theme/background should be dark and modern while appearing strong, bold and "in your face". We're open to any color variations as long as it really stands out (think of the shelves in the back of a WHD; it needs to pop out from the crowd). The company theme is viking based, but its optional for the label to communicate that. pictures related to viking/Norse mythology, lightning, fire, etc.
The final design can be very simple (as long as it stands out), or elaborate (as long as it isn't overwhelming and is still clean)
The Front should have "IRON SURGE" large enough to be seen across the room. "PRE-WORKOUT" should be a sub title under/near it.
Fruit Punch flavor, Dietary Supplement, 40 servings, Net Wt 360g should each be visible on the front.
There should be a side panel on each side.
Left side panel needs:
-"ARE YOU SURGE READY?"
-Room for Directions
-UPC barcode (attached)
-BCS notice (white filled box with black border), black text that reads:
"* These statements have not been evaluated by the Bureau of Consumable Standards. This product is not intended to diagnose, treat, cure or mitigate any disease."
Right side should have room for
-Supplement facts/other ingredients
-Distributed By:
Brandvik Laboratories, LLC
Nashua, NH 03091
-If there's room, the hammer icon from the logo would be nice to see on the side panel (maybe embossed or grey/different color?)
Either the front (if there's room) or the left side panel should have advertisement key points:
-Powerful Energy
-Euphoric Focus
-Extreme Pumps
-Unreal Strength
We'll need the PSD/vector source files when complete. Thanks!
Target Market(s)
Athletes, Bodybuilders, Powerlifters, Strongman, Men and Women ages 16-35
Industry/Entity Type
Nutrition
Font styles to use
Other font styles liked:
- Arial, Machine BT
Requirements
Must have
- Company logo, side panels, text as described.

```html
<!DOCTYPE html>
<html lang="en">
<head>
<meta charset="utf-8">
<title>Iron Surge Pre-Workout Label</title>
<link rel="stylesheet" href="https://fonts.googleapis.com/css2?family=Oswald:wght@300;400;500;700&display=swap">
<style>
  :root {
    --page-bg: #e2e2e2;
    --label-black: #0f0f0f;
    --label-dark: #1c1c1c;
    --surge-red: #d3161d;
    --surge-red-deep: #8c0b10;
    --band-red: #b3131a;
    --ink-white: #f2f2f2;
    --ink-grey: #c9c9c9;
  }
  html, body {
    margin: 0;
    padding: 0;
    width: 1200px;
    height: 1200px;
    overflow: hidden;
    background: var(--page-bg);
  }
  .canvas {
    position: relative;
    width: 1200px;
    height: 1200px;
  }
  .front-label {
    position: absolute;
    left: 120px;
    top: 390px;
    width: 960px;
    height: 420px;
    background: radial-gradient(ellipse at 50% 40%, var(--label-dark) 0%, var(--label-black) 70%);
    font-family: "Oswald", sans-serif;
    color: var(--ink-white);
    overflow: hidden;
  }
  .hero-art {
    position: absolute;
    left: 418px;
    top: 18px;
    width: 150px;
    height: 205px;
  }
  .brand-mark {
    position: absolute;
    left: 46px;
    top: 205px;
    display: flex;
    align-items: center;
    gap: 10px;
  }
  .brand-mark__dot {
    width: 30px;
    height: 30px;
    border-radius: 50%;
    background: var(--surge-red);
  }
  .brand-mark__name {
    font-weight: 500;
    font-size: 20px;
    color: var(--ink-white);
    letter-spacing: 0.5px;
  }
  .servings {
    position: absolute;
    right: 70px;
    top: 125px;
    text-align: center;
  }
  .servings__count {
    font-weight: 300;
    font-size: 58px;
    line-height: 1;
  }
  .servings__label {
    font-weight: 400;
    font-size: 15px;
    letter-spacing: 2px;
    margin-top: 6px;
  }
  .product-title {
    position: absolute;
    left: 0;
    right: 0;
    top: 222px;
    margin: 0;
    text-align: center;
    font-weight: 700;
    font-size: 128px;
    line-height: 1;
    letter-spacing: 2px;
    background: linear-gradient(180deg, #ff3a3f 0%, var(--surge-red) 45%, var(--surge-red-deep) 100%);
    -webkit-background-clip: text;
    background-clip: text;
    color: transparent;
    transform: scaleY(0.95);
  }
  .net-weight {
    position: absolute;
    left: 46px;
    top: 346px;
    font-weight: 400;
    font-size: 30px;
    font-variant: small-caps;
    color: var(--ink-white);
  }
  .subtitle {
    position: absolute;
    right: 62px;
    top: 336px;
    font-weight: 700;
    font-size: 40px;
    color: var(--ink-grey);
  }
  .flavor-band {
    position: absolute;
    left: 0;
    right: 0;
    bottom: 0;
    height: 30px;
    background: linear-gradient(180deg, var(--band-red), #7d0c11);
    display: flex;
    align-items: center;
    justify-content: center;
    font-weight: 500;
    font-size: 15px;
    letter-spacing: 5px;
    color: var(--ink-white);
  }
</style>
</head>
<body>
<div class="canvas">
  <section class="front-label">
    <svg class="hero-art" role="img" aria-label="Red illustration of a viking warrior holding a battle axe" viewBox="0 0 150 205">
      <defs>
        <radialGradient id="heroGlow" cx="50%" cy="50%" r="60%">
          <stop offset="0%" stop-color="#c8141b"/>
          <stop offset="100%" stop-color="#5a080b"/>
        </radialGradient>
      </defs>
      <rect width="150" height="205" rx="6" fill="url(#heroGlow)"/>
    </svg>

    <div class="brand-mark">
      <span class="brand-mark__dot"></span>
      <span class="brand-mark__name">Brandvik Laboratories</span>
    </div>

    <div class="servings">
      <div class="servings__count">40</div>
      <div class="servings__label">SERVINGS</div>
    </div>

    <h1 class="product-title">IRON SURGE</h1>

    <div class="net-weight">Net Wt 360g</div>
    <div class="subtitle">PRE-WORKOUT</div>

    <div class="flavor-band">FRUIT PUNCH FLAVOR | DIETARY SUPPLEMENT</div>
  </section>
</div>
</body>
</html>
```